Lotus Leaf Kitchen Road Billboard

Road Billboard I need all of this information on it
Authentic Thai Food Bangkok Style
6.5 Miles on the right
4126 Maple Ridge Rd Otto NC
828-555-4172

```html
<!DOCTYPE html>
<html lang="en">
<head>
<meta charset="utf-8">
<title>Lotus Leaf Kitchen Road Billboard</title>
<link rel="stylesheet" href="https://fonts.googleapis.com/css2?family=Bebas+Neue&display=swap">
<style>
  :root {
    --ink: #000000;
    --gold: #d8a917;
    --gold-bright: #e6b91f;
    --white: #ffffff;
    --page: #e8e8ec;
  }
  * { margin: 0; padding: 0; box-sizing: border-box; }
  html, body {
    width: 1200px;
    height: 817px;
    overflow: hidden;
    background: var(--page);
  }
  .billboard {
    position: absolute;
    left: 40px;
    top: 252px;
    width: 1120px;
    height: 312px;
    background: var(--gold);
    font-family: "Bebas Neue", "Oswald", sans-serif;
    color: var(--ink);
    overflow: hidden;
  }
  .billboard-shapes {
    position: absolute;
    inset: 0;
    width: 1120px;
    height: 312px;
  }
  .brand {
    position: absolute;
    left: 0;
    right: 0;
    top: 22px;
    display: flex;
    align-items: center;
    justify-content: center;
    gap: 28px;
  }
  .brand-mark {
    width: 84px;
    height: 84px;
    border-radius: 50%;
    background: var(--gold-bright);
  }
  .brand-name {
    font-size: 112px;
    line-height: 1;
    letter-spacing: 2px;
    color: var(--gold-bright);
    padding-top: 8px;
  }
  .info {
    position: absolute;
    top: 190px;
    bottom: 0;
    display: flex;
    flex-direction: column;
    justify-content: center;
    white-space: nowrap;
  }
  .info-small { font-size: 42px; line-height: 0.95; }
  .info-large { font-size: 72px; line-height: 0.95; }
  .info-address { left: 20px; width: 390px; }
  .info-address .info-small { font-size: 36px; }
  .info-food { left: 436px; width: 385px; }
  .info-distance { left: 850px; width: 260px; }
  .info-distance .info-small { letter-spacing: 2px; }
</style>
</head>
<body>
  <section class="billboard">
    <svg class="billboard-shapes" viewBox="0 0 1120 312" aria-hidden="true">
      <path class="header-band" d="M0 0 H1120 V148 C800 188 320 196 0 153 Z" fill="var(--ink)"/>
      <path class="route-arrow-line" d="M330 182 C600 192 860 180 1050 158" fill="none" stroke="var(--white)" stroke-width="5" stroke-linecap="round"/>
      <polyline class="route-arrow-head" points="1030,143 1054,157 1036,174" fill="none" stroke="var(--white)" stroke-width="6" stroke-linecap="round" stroke-linejoin="round"/>
      <rect class="column-divider" x="415" y="186" width="6" height="126" fill="var(--ink)"/>
      <rect class="column-divider" x="828" y="182" width="6" height="130" fill="var(--ink)"/>
    </svg>

    <header class="brand">
      <span class="brand-mark"></span>
      <h1 class="brand-name">Lotus Leaf Kitchen</h1>
    </header>

    <div class="info info-address">
      <p class="info-small">4126 Maple Ridge Rd Otto NC</p>
      <p class="info-large">828-555-4172</p>
    </div>

    <div class="info info-food">
      <p class="info-small">Authentic Thai Food</p>
      <p class="info-large">Bangkok Style</p>
    </div>

    <div class="info info-distance">
      <p class="info-small">6.5 Miles On</p>
      <p class="info-large">The Right</p>
    </div>
  </section>
</body>
</html>
```